Sport Planning Report/ Company Template (in powerpoint)

We need to create a new branded, cleaner and more professional set of slide templates. Includes title slide, content/ intro slide, main content slides, and final slide template. Format should be 16:9 (on screen show). These slides may include animation but the main focus is on the professional design and these will be converted to PDF and sent as reports too. Using the new template to redesign our Investment Planning standard report - example attached. This report is used across Australia and New Zealand to advise on the feasibility of new community leisure, aquatic and sport facilities. And the technical specification of these sites. This should be reflected in the theme of the report design. See www.brightplayhub.net for details on this service (half way down the homepage). Simplify the report format to between 5-10 slides. The same order of content in terms of sections. Ability to add and edit text, maps, tables and graphs using the template so new reports are fast to produce using the template. If possible the last slide would include a better version of the infographic which summarises our services. If any alternative colours or text is used (we are open to new fonts used) we will require the brand guidelines.

Target Market(s)

technical
community sport

Colors

Designer to choose colors to be used in the design.

Requirements
Must have
• Clean design
• On brand (see colouts)

```html
<!DOCTYPE html>
<html lang="en">
<head>
<meta charset="utf-8">
<title>BrightPlay Investment Planning Model – Slide Templates</title>
<link href="https://fonts.googleapis.com/css2?family=Roboto:wght@300;400;500;700;900&display=swap" rel="stylesheet">
<style>
:root{
  --purple:#5b2b9f;
  --purple-dark:#44207e;
  --purple-light:#7d4bc9;
  --green:#3fa535;
  --green-dark:#2b8a2f;
  --grey:#c9c9cc;
  --grey-light:#e6e6ea;
  --ink:#2b2b2b;
  --muted:#8b8b8f;
  --page:#f2f2f4;
  --white:#ffffff;
}
*{box-sizing:border-box;margin:0;padding:0}
html,body{width:1200px;height:4608px;overflow:hidden}
body{font-family:"Roboto",Arial,sans-serif;color:var(--ink);background:var(--page)}
.canvas{position:relative;width:1200px;height:4608px;overflow:hidden;background:var(--page)}
.abs{position:absolute}
.slide{position:absolute;width:560px;height:315px;background:var(--white);overflow:hidden;box-shadow:0 1px 4px rgba(0,0,0,.16)}
.col-l{left:27px}.col-r{left:615px}
.grad{background:linear-gradient(135deg,var(--purple-dark) 0%,var(--purple) 45%,var(--purple-light) 100%)}
.grad-green{background:linear-gradient(135deg,var(--green-dark),#4cb53f 60%,#2f9633)}
.brand{position:absolute;display:flex;align-items:center;gap:4px;font-weight:700;font-size:10px;color:var(--purple);letter-spacing:.2px}
.brand::before{content:"";width:7px;height:7px;border-radius:50%;background:var(--green)}
.brand--top{top:14px;right:16px}
.footer{position:absolute;left:0;right:0;bottom:0;height:9px;background:var(--purple);color:var(--white);font-size:6px;text-align:right;padding-right:24px;line-height:9px}
.footer::before{content:"";position:absolute;left:0;right:0;top:-3px;height:3px;background:var(--grey-light)}
.slide-title{position:absolute;left:26px;top:18px;font-size:17px;font-weight:500;color:var(--purple)}
.slide-title b{font-weight:700}
.slide-title span{color:var(--ink);font-weight:500}
.sub{font-size:7.5px;font-weight:700;color:var(--ink)}
.body{font-size:5.8px;line-height:1.6;color:#7a7a7e}
.body--light{color:rgba(255,255,255,.75)}
.date{position:absolute;left:16px;bottom:12px;font-size:5.5px;color:rgba(255,255,255,.6)}
.photo{position:absolute;background:linear-gradient(135deg,#6f7a84,#b9b3ad 55%,#4f5660)}
.photo--pool{background:linear-gradient(160deg,#2f8fc2,#6dc6e6 50%,#1c5f8f)}
.photo--gym{background:linear-gradient(135deg,#3b3b40,#8d8075 50%,#c9b9a7)}
.photo--warm{background:linear-gradient(135deg,#e7a45a,#c46a4a 50%,#5a3f6e)}
.bullets{list-style:none;font-size:5.5px;line-height:1.9;color:rgba(255,255,255,.8)}
.bullets li::before{content:"✓ ";color:var(--green)}
.bullets--dark{color:#7a7a7e}
/* hero */
.hero{position:absolute;left:220px;top:190px;width:760px;height:428px;background:var(--white);overflow:hidden;box-shadow:0 4px 18px rgba(0,0,0,.2)}
</style>
</head>
<body>
<main class="canvas">

<!-- Cover on screen -->
<section class="hero">
  <div class="abs grad" style="left:0;top:0;width:760px;height:200px"></div>
  <div class="abs" style="left:0;top:200px;width:760px;height:3px;background:var(--green)"></div>
  <div class="brand" style="left:50px;top:272px;font-size:15px">BrightPlay</div>
  <div class="abs" style="left:205px;top:250px;width:1px;height:70px;background:var(--grey)"></div>
  <h1 class="abs" style="left:232px;top:262px;font-size:25px;font-weight:500;color:var(--ink)">Title of presentation goes here</h1>
  <p class="abs" style="left:232px;top:300px;font-size:9px;color:var(--muted)">November 2019</p>
  <div class="abs" style="left:0;bottom:0;width:760px;height:16px;background:var(--purple)"></div>
</section>

<!-- Row 1 -->
<section class="slide col-l" style="top:822px">
  <div class="abs grad" style="left:0;top:0;width:560px;height:150px"></div>
  <div class="abs grad" style="left:0;top:212px;width:560px;height:103px"></div>
  <div class="abs" style="left:0;top:209px;width:560px;height:3px;background:var(--green)"></div>
  <div class="brand" style="left:14px;top:174px;font-size:11px">BrightPlay</div>
  <div class="abs" style="left:130px;top:158px;width:1px;height:44px;background:var(--grey)"></div>
  <p class="abs" style="left:142px;top:160px;font-size:8px;color:var(--muted)">Site Report</p>
  <h2 class="abs" style="left:142px;top:172px;font-size:15.5px;font-weight:700">BrightPlay Investment Planning Model</h2>
  <p class="date">November 2019</p>
</section>
<section class="slide col-r grad" style="top:822px">
  <div class="abs" style="left:0;top:0;width:560px;height:22px;background:var(--white)"></div>
  <div class="brand" style="left:14px;top:6px;font-size:9px">BrightPlay</div>
  <h2 class="abs" style="left:0;width:560px;top:148px;text-align:center;font-size:17px;font-weight:700;color:var(--white)">BrightPlay Investment Planning Model</h2>
  <p class="abs" style="left:0;width:560px;top:172px;text-align:center;font-size:9px;color:rgba(255,255,255,.55)">Site Report</p>
  <p class="date">November 2019</p>
</section>

<!-- Row 2 -->
<section class="slide col-l grad" style="top:1165px">
  <div class="abs" style="left:0;top:0;width:560px;height:22px;background:var(--white)"></div>
  <div class="brand" style="left:14px;top:6px;font-size:9px">BrightPlay</div>
  <h2 class="abs" style="left:0;width:560px;top:148px;text-align:center;font-size:17px;font-weight:700;color:var(--white)">BrightPlay Investment Planning Model</h2>
  <p class="abs" style="left:0;width:560px;top:172px;text-align:center;font-size:9px;color:rgba(255,255,255,.55)">Site Report</p>
  <p class="date">November 2019</p>
</section>
<section class="slide col-r grad" style="top:1165px">
  <div class="abs" style="left:0;top:285px;width:560px;height:30px;background:var(--white);border-top:3px solid var(--green)"></div>
  <div class="brand" style="left:36px;top:295px;font-size:9px">BrightPlay</div>
  <h2 class="abs" style="left:28px;top:120px;width:200px;font-size:15px;font-weight:700;color:var(--white);line-height:1.25">Report Structure - market intelligence applied locally</h2>
  <div class="abs" style="left:250px;top:40px;width:290px">
    <div style="display:flex;gap:10px;margin-bottom:32px">
      <div style="flex:0 0 22px;height:22px;background:var(--purple-light);color:#fff;font-size:9px;font-weight:700;display:flex;align-items:center;justify-content:center">01</div>
      <div><p style="font-size:6.5px;font-weight:700;color:#fff">Process overview – a sector first</p><p class="body body--light">New data from over 2 million community program and facility members sets participation trends and the performance of hundreds of facilities to model demand.</p></div>
    </div>
    <div style="display:flex;gap:10px;margin-bottom:32px">
      <div style="flex:0 0 22px;height:22px;background:var(--purple-light);color:#fff;font-size:9px;font-weight:700;display:flex;align-items:center;justify-content:center">02</div>
      <div><p style="font-size:6.5px;font-weight:700;color:#fff">Catchment overview</p><p class="body body--light">Location of the site, comparison of travel time across facilities and profile of demand segments.</p></div>
    </div>
    <div style="display:flex;gap:10px">
      <div style="flex:0 0 22px;height:22px;background:var(--purple-light);color:#fff;font-size:9px;font-weight:700;display:flex;align-items:center;justify-content:center">03</div>
      <div><p style="font-size:6.5px;font-weight:700;color:#fff">Projected demand + optimal offer</p><p class="body body--light">Projected members and visits by facility. Optimal program and facility mix to reflect the profile of the area, aligned with demand and capacity.</p></div>
    </div>
  </div>
</section>

<!-- Row 3 -->
<section class="slide col-l grad-green" style="top:1508px">
  <h2 class="abs" style="left:22px;top:110px;width:120px;font-size:17px;font-weight:700;color:#fff;line-height:1.1">Investment Planning Model</h2>
  <div class="abs" style="left:150px;top:34px;width:390px;display:grid;grid-template-columns:1fr 1fr;column-gap:24px;row-gap:26px">
    <div style="display:flex;gap:7px"><svg width="14" height="14" viewBox="0 0 14 14"><rect x="1" y="2" width="12" height="8" fill="none" stroke="#fff"/><path d="M5 12h4" stroke="#fff"/></svg><div><p style="font-size:6.5px;font-weight:700;color:#fff">Sector database – a sector first</p><p class="body body--light">Data from the largest member datasets across the sector informs benchmarks.</p></div></div>
    <div style="display:flex;gap:7px"><svg width="14" height="14" viewBox="0 0 14 14"><path d="M2 12V6M6 12V3M10 12V8" stroke="#fff" stroke-width="2"/></svg><div><p style="font-size:6.5px;font-weight:700;color:#fff">Model metrics</p><p class="body body--light">Over 100 metrics for each facility type, including catchment and travel time.</p></div></div>
    <div style="display:flex;gap:7px"><svg width="14" height="14" viewBox="0 0 14 14"><circle cx="6" cy="6" r="4" fill="none" stroke="#fff"/><path d="M9 9l4 4" stroke="#fff"/></svg><div><p style="font-size:6.5px;font-weight:700;color:#fff">Supply and competition</p><p class="body body--light">All existing facilities mapped with their capacity and offer.</p></div></div>
    <div style="display:flex;gap:7px"><svg width="14" height="14" viewBox="0 0 14 14"><circle cx="7" cy="4" r="3" fill="none" stroke="#fff"/><path d="M2 13c0-4 10-4 10 0" fill="none" stroke="#fff"/></svg><div><p style="font-size:6.5px;font-weight:700;color:#fff">Demand allocation</p><p class="body body--light">Members allocated to the most likely venue by travel time.</p></div></div>
    <div style="display:flex;gap:7px"><svg width="14" height="14" viewBox="0 0 14 14"><path d="M2 12L6 7l3 3 4-6" fill="none" stroke="#fff"/></svg><div><p style="font-size:6.5px;font-weight:700;color:#fff">Demand profiling</p><p class="body body--light">Demographic and lifestyle segments shape projected demand.</p></div></div>
    <div style="display:flex;gap:7px"><svg width="14" height="14" viewBox="0 0 14 14"><path d="M7 1C4 1 2 3 2 6c0 4 5 7 5 7s5-3 5-7c0-3-2-5-5-5z" fill="none" stroke="#fff"/></svg><div><p style="font-size:6.5px;font-weight:700;color:#fff">Validation</p><p class="body body--light">Results tested against similar operating facilities.</p></div></div>
  </div>
  <div class="abs" style="left:0;top:285px;width:560px;height:30px;background:var(--white);border-top:3px solid var(--purple)"></div>
  <div class="brand" style="left:26px;top:295px;font-size:9px">BrightPlay</div>
  <p class="abs" style="right:26px;top:298px;font-size:6px;color:var(--ink)">www.brightplayhub.net</p>
</section>
<section class="slide col-r" style="top:1508px">
  <div class="photo photo--pool" role="img" aria-label="Swimmer diving into an indoor pool" style="left:0;top:0;width:170px;height:306px"></div>
  <div class="abs" style="left:165px;top:55px;width:395px;height:42px;background:var(--purple)"></div>
  <h2 class="abs" style="left:200px;top:66px;font-size:15px;font-weight:700;color:#fff">Welcome Message</h2>
  <div class="brand brand--top">BrightPlay</div>
  <p class="abs sub" style="left:262px;top:125px">Replace Your Text Here</p>
  <p class="abs body" style="left:262px;top:140px;width:270px">Duis arcu tortor, suscipit eget, imperdiet nec, imperdiet iaculis, ipsum. Sed aliquam ultrices mauris. Integer ante arcu, accumsan a, consectetuer eget, posuere ut, mauris. Praesent adipiscing. Phasellus ullamcorper. Duis arcu tortor, suscipit eget, imperdiet nec, imperdiet iaculis, ipsum. Sed aliquam ultrices mauris. Integer ante arcu, accumsan a, consectetuer eget, posuere ut, mauris. Praesent adipiscing. Phasellus ullamcorper.</p>
  <div class="footer">7</div>
</section>

<!-- Row 4 -->
<section class="slide col-l" style="top:1851px">
  <div class="abs grad" style="left:0;top:0;width:218px;height:306px"></div>
  <h2 class="abs" style="left:30px;top:140px;font-size:17px;font-weight:500;color:#fff">Agenda</h2>
  <div class="brand brand--top">BrightPlay</div>
  <p class="abs" style="left:232px;top:73px;font-size:7px;font-weight:700">Start</p>
  <p class="abs" style="left:262px;top:73px;font-size:6px;font-weight:700">◷ 9h00</p>
  <p class="abs" style="left:232px;top:161px;font-size:7px;font-weight:700">Break</p>
  <p class="abs" style="left:262px;top:161px;font-size:6px;font-weight:700">◷ 12h00</p>
  <div class="abs" style="left:318px;top:78px;width:1px;height:168px;background:var(--purple)"></div>
  <div class="abs" style="left:314px;top:72px;width:220px;font-size:6px;color:#666;line-height:27.5px">
    <p><span style="color:var(--purple)">●</span>&nbsp;&nbsp;Lorem ipsum dolor sit amet</p>
    <p><span style="color:var(--purple)">●</span>&nbsp;&nbsp;Duis arcu tortor, suscipit eget</p>
    <p><span style="color:var(--purple)">●</span>&nbsp;&nbsp;Lorem ipsum dolor sit amet arcu tortor eget</p>
    <p><span style="color:var(--purple)">●</span>&nbsp;&nbsp;Duis arcu tortor, suscipit eget</p>
    <p><span style="color:var(--purple)">●</span>&nbsp;&nbsp;Duis arcu tortor</p>
    <p><span style="color:var(--purple)">●</span>&nbsp;&nbsp;Duis arcu tortor, suscipit eget</p>
    <p><span style="color:var(--purple)">●</span>&nbsp;&nbsp;Lorem ipsum dolor sit amet arcu tortor eget</p>
  </div>
  <div class="footer">15</div>
</section>
<section class="slide col-r" style="top:1851px">
  <div class="abs grad" style="left:0;top:0;width:560px;height:122px"></div>
  <div class="photo photo--warm" role="img" aria-label="Portrait of the co-founder" style="left:232px;top:70px;width:74px;height:74px;transform:rotate(45deg);border:3px solid #fff"></div>
  <h2 class="abs" style="left:34px;top:170px;font-size:16px;font-weight:700;color:var(--purple)">Welcome <span style="color:var(--ink);font-weight:500">Message</span></h2>
  <p class="abs sub" style="left:34px;top:200px">Sam Reed</p>
  <p class="abs" style="left:34px;top:210px;font-size:5px;font-weight:700;color:var(--green)">Co-Founder Ceo</p>
  <p class="abs body" style="left:34px;top:225px;width:420px">Duis arcu tortor, suscipit eget, imperdiet nec, imperdiet iaculis, ipsum. Sed aliquam ultrices mauris. Integer ante arcu, accumsan a, consectetuer eget, posuere ut, mauris. Praesent adipiscing. Phasellus ullamcorper. Duis arcu tortor, suscipit eget, imperdiet nec.</p>
  <div class="footer">14</div>
</section>

<!-- Row 5 -->
<section class="slide col-l" style="top:2194px">
  <h2 class="slide-title"><b>About Us</b></h2>
  <div class="brand brand--top">BrightPlay</div>
  <div class="abs grad" style="left:0;top:60px;width:560px;height:92px"></div>
  <div class="photo photo--gym" role="img" aria-label="Runner lacing trainers on a track" style="left:230px;top:60px;width:330px;height:92px"></div>
  <ul class="abs bullets" style="left:30px;top:78px"><li>Duis arcu tortor, suscipit eget, imperdiet nec</li><li>Sed aliquam ultrices mauris. Integer ante arcu</li><li>Consectetuer eget, posuere ut, mauris</li><li>Praesent adipiscing</li></ul>
  <p class="abs sub" style="left:26px;top:188px">Replace Your Text Here</p>
  <p class="abs body" style="left:26px;top:203px;width:508px">Duis arcu tortor, suscipit eget, imperdiet nec, imperdiet iaculis, ipsum. Sed aliquam ultrices mauris. Integer ante arcu, accumsan a, consectetuer eget, posuere ut, mauris. Praesent adipiscing. Phasellus ullamcorper. Duis arcu tortor, suscipit eget, imperdiet nec, imperdiet iaculis, ipsum. Sed aliquam ultrices mauris. Integer ante arcu, accumsan a, consectetuer eget, posuere ut, mauris. Praesent adipiscing. Phasellus ullamcorper. Duis arcu tortor, suscipit eget, imperdiet nec, imperdiet iaculis, ipsum.</p>
  <div class="footer">8</div>
</section>
<section class="slide col-r" style="top:2194px">
  <h2 class="slide-title"><b>About Us</b></h2>
  <div class="brand brand--top">BrightPlay</div>
  <p class="abs sub" style="left:26px;top:62px">Replace Your Text Here</p>
  <p class="abs body" style="left:26px;top:78px;width:290px">Duis arcu tortor, suscipit eget, imperdiet nec, imperdiet iaculis, ipsum. Sed aliquam ultrices mauris. Integer ante arcu, accumsan a, consectetuer eget, posuere ut, mauris. Praesent adipiscing. Phasellus ullamcorper. Duis arcu tortor, suscipit eget, imperdiet nec, imperdiet iaculis, ipsum. Sed aliquam ultrices mauris. Integer ante arcu, accumsan a, consectetuer eget, posuere ut, mauris. Praesent adipiscing. Phasellus ullamcorper. Duis arcu tortor, suscipit eget, imperdiet nec, imperdiet iaculis, ipsum.<br><br>Duis arcu tortor, suscipit eget, imperdiet nec, imperdiet iaculis, ipsum. Sed aliquam ultrices mauris. Integer ante arcu, accumsan a, consectetuer eget, posuere ut, mauris.</p>
  <div class="photo photo--gym" role="img" aria-label="Group fitness class lifting weights" style="left:335px;top:48px;width:170px;height:228px"></div>
  <div class="footer">9</div>
</section>

<!-- Row 6 -->
<section class="slide col-l" style="top:2537px">
  <div class="abs grad" style="left:0;top:0;width:205px;height:306px"></div>
  <h2 class="abs" style="left:32px;top:88px;font-size:15px;font-weight:500;color:#fff;letter-spacing:.5px">Title goes here</h2>
  <p class="abs body body--light" style="left:32px;top:112px;width:150px">Duis arcu tortor, suscipit eget, imperdiet nec, imperdiet iaculis, ipsum. Sed aliquam ultrices mauris. Integer ante arcu, accumsan a, consectetuer eget, posuere ut, mauris.</p>
  <div class="abs" role="img" aria-label="Services infographic summarising the planning network" style="left:300px;top:28px;width:180px;height:262px;background:linear-gradient(180deg,#f3effa,#e3d8f3 60%,#d8ecd6)"></div>
  <div class="abs" style="left:205px;right:0;bottom:0;height:9px;background:var(--purple);color:#fff;font-size:6px;text-align:right;padding-right:24px;line-height:9px">13</div>
</section>
<section class="slide col-r grad" style="top:2537px">
  <h2 class="abs" style="left:26px;top:142px;font-size:18px;font-weight:500;color:#fff;letter-spacing:.5px">01&nbsp;&nbsp;Section Slide</h2>
  <p class="abs body body--light" style="left:62px;top:170px;width:270px">Duis arcu tortor, suscipit eget, imperdiet nec, imperdiet iaculis, ipsum. Sed aliquam ultrices mauris. Integer ante arcu, accumsan a, consectetuer eget, posuere ut, mauris.</p>
</section>

<!-- Row 7 -->
<section class="slide col-l" style="top:2880px">
  <h2 class="slide-title" style="font-size:14px"><b>Image at</b> <span>top and text</span></h2>
  <div class="brand brand--top">BrightPlay</div>
  <div class="photo photo--pool" role="img" aria-label="Swimmer mid-stroke in a lane" style="left:0;top:50px;width:560px;height:108px"></div>
  <p class="abs sub" style="left:26px;top:172px">Replace Your Text Here</p>
  <p class="abs body" style="left:26px;top:187px;width:508px">Duis arcu tortor, suscipit eget, imperdiet nec, imperdiet iaculis, ipsum. Sed aliquam ultrices mauris. Integer ante arcu, accumsan a, consectetuer eget, posuere ut, mauris. Praesent adipiscing. Phasellus ullamcorper. Duis arcu tortor, suscipit eget, imperdiet nec, imperdiet iaculis, ipsum. Sed aliquam ultrices mauris.</p>
  <div class="footer">21</div>
</section>
<section class="slide col-r" style="top:2880px">
  <h2 class="slide-title"><b>Our</b> <span>Process</span></h2>
  <div class="brand brand--top">BrightPlay</div>
  <svg class="abs" style="left:38px;top:66px" width="490" height="46" viewBox="0 0 490 46">
    <polygon points="0,0 104,0 122,23 104,46 0,46 18,23" fill="var(--purple)"/>
    <polygon points="124,0 228,0 246,23 228,46 124,46 142,23" fill="#d6d6da"/>
    <polygon points="248,0 352,0 370,23 352,46 248,46 266,23" fill="#d6d6da"/>
    <polygon points="372,0 472,0 490,23 472,46 372,46 390,23" fill="#d6d6da"/>
    <g font-family="Roboto,Arial,sans-serif" font-size="14" font-weight="700" fill="#fff" text-anchor="middle">
      <text x="64" y="28">01</text><text x="188" y="28">02</text><text x="312" y="28">03</text><text x="434" y="28">04</text>
    </g>
  </svg>
  <div class="abs" style="left:44px;top:124px;width:490px;display:grid;grid-template-columns:repeat(4,1fr);column-gap:14px">
    <div><p style="font-size:6px;font-weight:700">Replace your text here</p><ul class="bullets bullets--dark" style="font-size:5px;line-height:1.7"><li>Duis arcu tortor, suscipit eget, imperdiet nec</li><li>Sed aliquam ultrices mauris</li><li>Consectetuer eget, posuere ut</li><li>Praesent adipiscing</li></ul></div>
    <div><p style="font-size:6px;font-weight:700">Replace your text here</p><ul class="bullets bullets--dark" style="font-size:5px;line-height:1.7"><li>Duis arcu tortor, suscipit eget, imperdiet nec</li><li>Sed aliquam ultrices mauris</li><li>Consectetuer eget, posuere ut</li><li>Praesent adipiscing</li></ul></div>
    <div><p style="font-size:6px;font-weight:700">Replace your text here</p><ul class="bullets bullets--dark" style="font-size:5px;line-height:1.7"><li>Duis arcu tortor, suscipit eget, imperdiet nec</li><li>Sed aliquam ultrices mauris</li><li>Consectetuer eget, posuere ut</li><li>Praesent adipiscing</li></ul></div>
    <div><p style="font-size:6px;font-weight:700">Replace your text here</p><ul class="bullets bullets--dark" style="font-size:5px;line-height:1.7"><li>Duis arcu tortor, suscipit eget, imperdiet nec</li><li>Sed aliquam ultrices mauris</li><li>Consectetuer eget, posuere ut</li><li>Praesent adipiscing</li></ul></div>
  </div>
  <div class="footer">10</div>
</section>

<!-- Row 8 -->
<section class="slide col-l" style="top:3223px">
  <h2 class="slide-title"><b>Numbered</b> <span>Slide</span></h2>
  <div class="brand brand--top">BrightPlay</div>
  <div class="abs" style="left:26px;top:85px;width:510px;display:grid;grid-template-columns:repeat(3,1fr);row-gap:36px;column-gap:16px;font-size:6px">
    <div style="display:flex;gap:6px"><span style="flex:0 0 14px;height:14px;border-radius:50%;background:var(--purple);color:#fff;font-size:5px;display:flex;align-items:center;justify-content:center">01</span><div><p style="font-weight:700">Company Profile</p><p class="body" style="font-size:5px">Lorem ipsum dolor sit amet consectetur adipiscing elit sed do.</p></div></div>
    <div style="display:flex;gap:6px"><span style="flex:0 0 14px;height:14px;border-radius:50%;background:var(--purple);color:#fff;font-size:5px;display:flex;align-items:center;justify-content:center">02</span><div><p style="font-weight:700">Diagrams &amp; Flowcharts</p><p class="body" style="font-size:5px">Lorem ipsum dolor sit amet consectetur adipiscing elit sed do.</p></div></div>
    <div style="display:flex;gap:6px"><span style="flex:0 0 14px;height:14px;border-radius:50%;background:var(--purple);color:#fff;font-size:5px;display:flex;align-items:center;justify-content:center">03</span><div><p style="font-weight:700">Section Divider</p><p class="body" style="font-size:5px">Lorem ipsum dolor sit amet consectetur adipiscing elit sed do.</p></div></div>
    <div style="display:flex;gap:6px"><span style="flex:0 0 14px;height:14px;border-radius:50%;background:var(--purple);color:#fff;font-size:5px;display:flex;align-items:center;justify-content:center">04</span><div><p style="font-weight:700">Portfolio Design</p><p class="body" style="font-size:5px">Lorem ipsum dolor sit amet consectetur adipiscing elit sed do.</p></div></div>
    <div style="display:flex;gap:6px"><span style="flex:0 0 14px;height:14px;border-radius:50%;background:var(--purple);color:#fff;font-size:5px;display:flex;align-items:center;justify-content:center">05</span><div><p style="font-weight:700">Dashboard Design</p><p class="body" style="font-size:5px">Lorem ipsum dolor sit amet consectetur adipiscing elit sed do.</p></div></div>
    <div style="display:flex;gap:6px"><span style="flex:0 0 14px;height:14px;border-radius:50%;background:var(--purple);color:#fff;font-size:5px;display:flex;align-items:center;justify-content:center">06</span><div><p style="font-weight:700">Graphic Charts</p><p class="body" style="font-size:5px">Lorem ipsum dolor sit amet consectetur adipiscing elit sed do.</p></div></div>
    <div style="display:flex;gap:6px"><span style="flex:0 0 14px;height:14px;border-radius:50%;background:var(--purple);color:#fff;font-size:5px;display:flex;align-items:center;justify-content:center">07</span><div><p style="font-weight:700">Infographics Elements</p><p class="body" style="font-size:5px">Lorem ipsum dolor sit amet consectetur adipiscing elit sed do.</p></div></div>
    <div style="display:flex;gap:6px"><span style="flex:0 0 14px;height:14px;border-radius:50%;background:var(--purple);color:#fff;font-size:5px;display:flex;align-items:center;justify-content:center">08</span><div><p style="font-weight:700">World Map Infographics</p><p class="body" style="font-size:5px">Lorem ipsum dolor sit amet consectetur adipiscing elit sed do.</p></div></div>
  </div>
  <div class="footer">11</div>
</section>
<section class="slide col-r" style="top:3223px">
  <h2 class="slide-title"><b>Timeline</b></h2>
  <div class="brand brand--top">BrightPlay</div>
  <svg class="abs" style="left:0;top:0" width="560" height="300" viewBox="0 0 560 300">
    <g stroke="var(--grey)" stroke-width="1"><line x1="45" y1="115" x2="45" y2="148"/><line x1="235" y1="115" x2="235" y2="148"/><line x1="425" y1="115" x2="425" y2="148"/><line x1="140" y1="176" x2="140" y2="200"/><line x1="330" y1="176" x2="330" y2="200"/></g>
    <rect x="25" y="148" width="505" height="28" rx="14" fill="#c4c4c8"/>
    <circle cx="45" cy="162" r="15" fill="var(--purple)" stroke="#fff" stroke-width="2"/>
    <g fill="#9c9ca2" stroke="#fff" stroke-width="2"><circle cx="140" cy="162" r="15"/><circle cx="235" cy="162" r="15"/><circle cx="330" cy="162" r="15"/><circle cx="425" cy="162" r="15"/></g>
    <g fill="none" stroke="#fff" stroke-width="1.4"><path d="M40 167l10-10M44 157h6v6"/><path d="M134 168v-6M139 168v-9M144 168v-4"/><circle cx="235" cy="162" r="5"/><path d="M325 167h10v-7h-10z"/><circle cx="425" cy="160" r="4"/><path d="M421 168h8"/></g>
  </svg>
  <div class="abs" style="left:30px;top:78px;width:110px"><p style="font-size:5px;color:#666">2008</p><p style="font-size:6.5px;font-weight:700;color:var(--purple)">Replace Your Text Here</p><p class="body" style="font-size:5px">Duis arcu tortor, suscipit eget, dolor sit imperdiet nec.</p></div>
  <div class="abs" style="left:222px;top:78px;width:110px"><p style="font-size:5px;color:#666">2010</p><p style="font-size:6.5px;font-weight:700;color:var(--ink)">Replace Your Text Here</p><p class="body" style="font-size:5px">Duis arcu tortor, suscipit eget, dolor sit imperdiet nec.</p></div>
  <div class="abs" style="left:412px;top:78px;width:110px"><p style="font-size:5px;color:#666">2018</p><p style="font-size:6.5px;font-weight:700;color:var(--ink)">Replace Your Text Here</p><p class="body" style="font-size:5px">Duis arcu tortor, suscipit eget, dolor sit imperdiet nec.</p></div>
  <div class="abs" style="left:147px;top:196px;width:110px"><p style="font-size:5px;color:#666">2009</p><p style="font-size:6.5px;font-weight:700;color:var(--ink)">Replace Your Text Here</p><p class="body" style="font-size:5px">Duis arcu tortor, suscipit eget, dolor sit imperdiet nec.</p></div>
  <div class="abs" style="left:337px;top:196px;width:110px"><p style="font-size:5px;color:#666">2012</p><p style="font-size:6.5px;font-weight:700;color:var(--ink)">Replace Your Text Here</p><p class="body" style="font-size:5px">Duis arcu tortor, suscipit eget, dolor sit imperdiet nec.</p></div>
  <div class="footer">24</div>
</section>

<!-- Row 9 -->
<section class="slide col-l" style="top:3566px">
  <h2 class="slide-title"><b>Diagram</b> <span>Slide</span></h2>
  <div class="brand brand--top">BrightPlay</div>
  <svg class="abs" style="left:190px;top:62px" width="180" height="180" viewBox="0 0 200 200">
    <circle cx="100" cy="100" r="45" fill="none" stroke="#c4c4c8" stroke-width="32" stroke-dasharray="45.1 2" transform="rotate(-89 100 100)"/>
    <circle cx="100" cy="100" r="45" fill="none" stroke="var(--purple)" stroke-width="32" stroke-dasharray="45.1 237.6" transform="rotate(-89 100 100)"/>
    <g font-family="Roboto,Arial,sans-serif" font-size="11" font-weight="700" fill="#fff" text-anchor="middle">
      <text x="122.5" y="65">01</text><text x="145" y="104">02</text><text x="122.5" y="143">03</text><text x="77.5" y="143">04</text><text x="55" y="104">05</text><text x="77.5" y="65">06</text>
    </g>
  </svg>
  <div class="abs" style="left:60px;top:82px;width:128px;text-align:right;font-size:5px;line-height:1.5;color:#888">
    <p style="font-weight:700;color:var(--ink);font-size:6px">Replace your text</p><p>Aenean commodo ligula eget dolor. Neque porro quisquam est.</p>
    <p style="font-weight:700;color:var(--ink);font-size:6px;margin-top:24px">Replace your text</p><p>Aenean commodo ligula eget dolor. Neque porro quisquam est.</p>
    <p style="font-weight:700;color:var(--ink);font-size:6px;margin-top:24px">Replace your text</p><p>Aenean commodo ligula eget dolor. Neque porro quisquam est.</p>
  </div>
  <div class="abs" style="left:380px;top:82px;width:128px;font-size:5px;line-height:1.5;color:#888">
    <p style="font-weight:700;color:var(--purple);font-size:6px">Replace your text</p><p>Aenean commodo ligula eget dolor. Neque porro quisquam est.</p>
    <p style="font-weight:700;color:var(--ink);font-size:6px;margin-top:24px">Replace your text</p><p>Aenean commodo ligula eget dolor. Neque porro quisquam est.</p>
    <p style="font-weight:700;color:var(--ink);font-size:6px;margin-top:24px">Replace your text</p><p>Aenean commodo ligula eget dolor. Neque porro quisquam est.</p>
  </div>
  <div class="footer">20</div>
</section>
<section class="slide col-r" style="top:3566px">
  <h2 class="slide-title"><b>Portfolio</b></h2>
  <div class="brand brand--top">BrightPlay</div>
  <div class="photo photo--gym" role="img" aria-label="Athlete tying running shoes" style="left:12px;top:55px;width:126px;height:120px"></div>
  <div class="photo" role="img" aria-label="Boxer wrapping hands" style="left:150px;top:55px;width:126px;height:120px;background:linear-gradient(135deg,#2d3a4c,#6c7f96 60%,#1e2530)"></div>
  <div class="photo photo--warm" role="img" aria-label="Runner on outdoor steps" style="left:288px;top:55px;width:126px;height:120px"></div>
  <div class="photo photo--gym" role="img" aria-label="Athlete stretching on a track" style="left:426px;top:55px;width:126px;height:120px"></div>
  <div class="abs" style="left:12px;top:185px;width:540px;display:grid;grid-template-columns:repeat(4,1fr);column-gap:12px;text-align:center">
    <div><p style="font-size:6.5px;font-weight:700">Replace Your Text Here</p><p class="body" style="font-size:5px">Imperdiet nec, imperdiet iaculis, ipsum. Lorem ipsum dolor sit ame.</p></div>
    <div><p style="font-size:6.5px;font-weight:700">Replace Your Text Here</p><p class="body" style="font-size:5px">Imperdiet nec, imperdiet iaculis, ipsum. Lorem ipsum dolor sit ame.</p></div>
    <div><p style="font-size:6.5px;font-weight:700">Replace Your Text Here</p><p class="body" style="font-size:5px">Imperdiet nec, imperdiet iaculis, ipsum. Lorem ipsum dolor sit ame.</p></div>
    <div><p style="font-size:6.5px;font-weight:700">Replace Your Text Here</p><p class="body" style="font-size:5px">Imperdiet nec, imperdiet iaculis, ipsum. Lorem ipsum dolor sit ame.</p></div>
  </div>
  <div class="footer">23</div>
</section>

<!-- Row 10 -->
<section class="slide col-l" style="top:3909px">
  <h2 class="slide-title" style="font-size:15px"><b>Three Column</b> <span>Slide with image</span></h2>
  <div class="brand brand--top">BrightPlay</div>
  <div class="photo" role="img" aria-label="Woman doing push-ups on a mat" style="left:60px;top:70px;width:140px;height:108px;clip-path:polygon(18% 0,100% 0,82% 100%,0 100%);background:linear-gradient(135deg,#e8e3e6,#d46a9a 60%,#8b6c8f)"></div>
  <div class="photo photo--warm" role="img" aria-label="Spin class on exercise bikes" style="left:210px;top:70px;width:140px;height:108px;clip-path:polygon(18% 0,100% 0,82% 100%,0 100%)"></div>
  <div class="photo" role="img" aria-label="Cyclists training indoors" style="left:360px;top:70px;width:140px;height:108px;clip-path:polygon(18% 0,100% 0,82% 100%,0 100%);background:linear-gradient(135deg,#2c3e70,#6f8ccd 55%,#273457)"></div>
  <div class="abs" style="left:50px;top:200px;width:460px;display:grid;grid-template-columns:repeat(3,1fr);column-gap:20px">
    <div><p style="font-size:6.5px;font-weight:700">Replace Your Text Here</p><p class="body" style="font-size:5px">Imperdiet nec, imperdiet iaculis, ipsum. Lorem ipsum dolor sit amet.</p></div>
    <div><p style="font-size:6.5px;font-weight:700">Replace Your Text Here</p><p class="body" style="font-size:5px">Imperdiet nec, imperdiet iaculis, ipsum. Lorem ipsum dolor sit amet.</p></div>
    <div><p style="font-size:6.5px;font-weight:700">Replace Your Text Here</p><p class="body" style="font-size:5px">Imperdiet nec, imperdiet iaculis, ipsum. Lorem ipsum dolor sit amet.</p></div>
  </div>
  <div class="footer">19</div>
</section>
<section class="slide col-r" style="top:3909px">
  <h2 class="slide-title" style="font-size:15px"><b>Two Column</b> <span>Slide with image</span></h2>
  <div class="brand brand--top">BrightPlay</div>
  <div class="photo photo--gym" role="img" aria-label="Gym floor with cardio machines" style="left:28px;top:55px;width:240px;height:90px"></div>
  <div class="photo" role="img" aria-label="Rowing machines in a fitness centre" style="left:292px;top:55px;width:240px;height:90px;background:linear-gradient(135deg,#4a5a6e,#a9b6c4 55%,#36404c)"></div>
  <div class="abs" style="left:28px;top:160px;width:504px;display:grid;grid-template-columns:1fr 1fr;column-gap:24px;text-align:center">
    <div><p style="font-size:6.5px;font-weight:700">Replace Your Text Here</p><p class="body" style="margin-top:6px">Duis arcu tortor, suscipit eget, imperdiet nec, imperdiet iaculis, ipsum. Sed aliquam ultrices mauris. Integer ante arcu, accumsan a, consectetuer eget, posuere ut, mauris. Praesent adipiscing. Phasellus ullamcorper.</p></div>
    <div><p style="font-size:6.5px;font-weight:700">Replace Your Text Here</p><p class="body" style="margin-top:6px">Duis arcu tortor, suscipit eget, imperdiet nec, imperdiet iaculis, ipsum. Sed aliquam ultrices mauris. Integer ante arcu, accumsan a, consectetuer eget, posuere ut, mauris. Praesent adipiscing. Phasellus ullamcorper.</p></div>
  </div>
  <div class="footer">22</div>
</section>

<!-- Row 11 -->
<section class="slide col-l" style="top:4252px">
  <h2 class="slide-title" style="font-size:15px"><b>Two Column</b> <span>Slide</span></h2>
  <div class="brand brand--top">BrightPlay</div>
  <div class="abs" style="left:26px;top:60px;width:508px;display:grid;grid-template-columns:1fr 1fr;column-gap:24px">
    <div><p class="sub" style="font-size:6.5px">Replace Your Text Here</p><p class="body" style="margin-top:10px">Duis arcu tortor, suscipit eget, imperdiet nec, imperdiet iaculis, ipsum. Sed aliquam ultrices mauris. Integer ante arcu, accumsan a, consectetuer eget, posuere ut, mauris. Praesent adipiscing. Phasellus ullamcorper. Duis arcu tortor, suscipit eget, imperdiet nec, imperdiet iaculis, ipsum. Sed aliquam ultrices mauris. Integer ante arcu, accumsan a, consectetuer eget, posuere ut, mauris. Praesent adipiscing. Phasellus ullamcorper.<br><br>Duis arcu tortor, suscipit eget, imperdiet nec, imperdiet iaculis, ipsum. Sed aliquam ultrices mauris. Integer ante arcu, accumsan a, consectetuer eget, posuere ut, mauris.</p></div>
    <div><p class="sub" style="font-size:6.5px">Replace Your Text Here</p><p class="body" style="margin-top:10px">Duis arcu tortor, suscipit eget, imperdiet nec, imperdiet iaculis, ipsum. Sed aliquam ultrices mauris. Integer ante arcu, accumsan a, consectetuer eget, posuere ut, mauris. Praesent adipiscing. Phasellus ullamcorper. Duis arcu tortor, suscipit eget, imperdiet nec, imperdiet iaculis, ipsum. Sed aliquam ultrices mauris. Integer ante arcu, accumsan a, consectetuer eget, posuere ut, mauris. Praesent adipiscing. Phasellus ullamcorper.<br><br>Duis arcu tortor, suscipit eget, imperdiet nec, imperdiet iaculis, ipsum. Sed aliquam ultrices mauris. Integer ante arcu, accumsan a, consectetuer eget, posuere ut, mauris.</p></div>
  </div>
  <div class="footer">17</div>
</section>
<section class="slide col-r" style="top:4252px">
  <h2 class="slide-title" style="font-size:15px"><b>One Column</b> <span>Slide</span></h2>
  <div class="brand brand--top">BrightPlay</div>
  <p class="abs sub" style="left:26px;top:60px;font-size:6.5px">Replace Your Text Here</p>
  <p class="abs body" style="left:26px;top:76px;width:508px">Duis arcu tortor, suscipit eget, imperdiet nec, imperdiet iaculis, ipsum. Sed aliquam ultrices mauris. Integer ante arcu, accumsan a, consectetuer eget, posuere ut, mauris. Praesent adipiscing. Phasellus ullamcorper. Duis arcu tortor, suscipit eget, imperdiet nec, imperdiet iaculis, ipsum. Sed aliquam ultrices mauris. Integer ante arcu, accumsan a, consectetuer eget, posuere ut, mauris. Praesent adipiscing. Phasellus ullamcorper. Duis arcu tortor, suscipit eget, imperdiet nec, imperdiet iaculis, ipsum. Sed aliquam ultrices mauris.<br><br>Duis arcu tortor, suscipit eget, imperdiet nec, imperdiet iaculis, ipsum. Sed aliquam ultrices mauris. Integer ante arcu, accumsan a, consectetuer eget, posuere ut, mauris. Praesent adipiscing. Phasellus ullamcorper. Duis arcu tortor, suscipit eget, imperdiet nec, imperdiet iaculis, ipsum. Sed aliquam ultrices mauris. Integer ante arcu, accumsan a, consectetuer eget, posuere ut, mauris. Praesent adipiscing. Phasellus ullamcorper.</p>
  <div class="footer">16</div>
</section>

</main>
</body>
</html>
```